Design signage for shop front glass windows

Our clinic is called Wattlebrook Medical Practice and we are a general practice offering medical services. Our services include
1. General Practice Consultations
2. Immunisations
3. Health checks
4. Women's health
5. Men's Health
6. Skin cancer checks
7. Travel medicine
8. Referrals
9. Antenatal checks
10. Minor surgery
11. Cosmetic medicine
12. Pre Employment Medicals
13. Diabetes care
14. Wound care
and much more

Our motto is
"friendly and professional health care for you and your family"

We also have a range of allied health services
including
Psychology
Physiotherapy
Podiatry
Dietetics and Nutrition
Exercise Physiology
Diabetes Education

On the signs there should be the words "Bulk Billing for GP services'
"Book online at www.wattlebrookmedicalpractice.example.au"
"Ph: 07 5196 4208"

We have glass windows on our shopfront - there are 11 panels (see attached photos) - 3 panels on the left have a white film and 4 panels in the centre are just tinted (no further signage will be installed on the central glass doors which are not included). There are another 4 panels on the right that have a white film. We are looking for a design for the glass signage to promote our services. We will print signage that can be stuck on the glass. There will need to be more bold signage on the white film and more subtle minor signage on the tinted glass windows which can still allow light thru. I have attached pictures of the window. Our logo is on our website www.wattlebrookmedicalpractice.example.au to get an idea of colours.

Target Market(s)

Young families living in the region of Capalaba Queensland

Industry/Entity Type

Health Care

Font styles to use
Serif

Colors
85abd2
acd036
ec1f27

Requirements
Must have
• The words
• "Bulk Billing for General Practice Services"
• "friendly and professional health care for you and your family"
• Book online at www.wattlebrookmedicalpractice.example.au
• Phone 07 5196 4208

```html
<!DOCTYPE html>
<html lang="en">
<head>
<meta charset="utf-8">
<title>Wattlebrook Medical Practice – Window Signage</title>
<link href="https://fonts.googleapis.com/css2?family=Roboto+Slab:wght@400;700;900&family=Tinos&display=swap" rel="stylesheet">
<style>
:root{
  --green:#acd036;
  --green-light:#d6ea96;
  --green-deep:#1f8a3a;
  --blue:#85abd2;
  --red:#ec1f27;
  --charcoal:#49494b;
  --charcoal-soft:#5a5a5d;
  --ink:#2a2a2a;
  --page:#ffffff;
}
*{margin:0;padding:0;box-sizing:border-box}
html,body{width:1200px;height:1200px;overflow:hidden;background:var(--page)}
.stage{width:1500px;height:1500px;transform:scale(.8);transform-origin:0 0;position:relative}
.strip{position:absolute;left:22px;top:620px;width:1456px;height:258px;display:flex;gap:4px}
.panel{flex:1;position:relative;overflow:hidden;font-family:"Roboto Slab",serif}
.panel--film{background:linear-gradient(180deg,var(--green-light) 0%,#c4df6a 50%,var(--green) 100%)}
.panel--tint{background:var(--charcoal)}
.photo{position:absolute;left:0;right:0;top:0}
.photo--desk{height:150px;background:linear-gradient(180deg,#e9ecef 0%,#d7dde0 55%,rgba(214,234,150,0) 100%)}
.photo--warm{height:150px;background:linear-gradient(180deg,#8c7a5a 0%,#b8ae7e 55%,rgba(214,234,150,0) 100%)}
.photo--clinic{height:160px;background:linear-gradient(180deg,#7d8890 0%,#b9c3c5 55%,rgba(214,234,150,0) 100%)}
.photo--hands{top:auto;bottom:0;height:130px;background:linear-gradient(0deg,#d9a7a0 0%,#c98e8a 45%,rgba(214,234,150,0) 100%)}
.headline{position:absolute;right:14px;text-align:right;font-weight:900;line-height:.95;white-space:nowrap}
.red{color:var(--red)}
.blue{color:var(--blue)}
.brand{position:absolute;left:14px;font-family:"Roboto Slab",serif;font-weight:700;font-size:8.5px;color:var(--green-deep);white-space:nowrap}
.brand--tint{color:var(--green)}
.motto{position:absolute;left:14px;font-family:"Tinos",serif;font-size:6px;line-height:1.15;color:var(--ink)}
.pulse{position:absolute;left:14px;top:216px;width:100px;height:8px;background:linear-gradient(90deg,rgba(133,171,210,.15),rgba(133,171,210,.55),rgba(133,171,210,.15))}
.pattern{position:absolute;bottom:0;height:80px;background:radial-gradient(ellipse at center,var(--charcoal-soft) 0%,rgba(73,73,75,0) 70%)}
.pattern--wide{left:0;right:0}
.tint-head{position:absolute;left:12px;font-weight:700;font-size:8.5px;color:var(--blue);white-space:nowrap}
.allied{position:absolute;left:12px;top:60px;list-style:none}
.allied li{font-weight:700;font-size:8.5px;color:var(--blue);height:21.5px;white-space:nowrap}
.allied li::before{content:"·";margin-right:8px}
.hours{position:absolute;left:14px;top:68px;font-family:"Tinos",serif;font-size:6.5px;color:var(--blue);border-collapse:collapse}
.hours td{padding:0 10px 0 0;line-height:8.3px;white-space:nowrap}
.note{position:absolute;left:14px;top:150px;font-family:"Tinos",serif;font-size:6.5px;color:var(--blue)}
.services{position:absolute;left:12px;top:63px;list-style:none;font-family:"Tinos",serif;font-size:5.6px;color:var(--blue)}
.services li{display:flex;line-height:9.1px}
.services li span{width:22px;flex:none}
.center-copy{position:absolute;left:0;right:0;text-align:center;font-weight:700;font-size:8px;color:var(--blue);line-height:1.3}
.cross{position:absolute;left:18px;top:110px;width:20px;height:20px}
</style>
</head>
<body>
<div class="stage">
  <div class="strip">

    <section class="panel panel--film">
      <div class="photo photo--desk" role="img" aria-label="Stethoscope and tablet on a white desk"></div>
      <div class="headline" style="top:110px">
        <div class="red" style="font-size:21px">CALL</div>
        <div class="blue" style="font-size:12px">us</div>
        <div class="red" style="font-size:14px;margin-top:3px">07 5196 4208</div>
      </div>
      <div class="brand" style="top:192px">Wattlebrook Medical Practice</div>
      <div class="pulse" role="img" aria-label="Heartbeat line ornament"></div>
      <p class="motto" style="top:229px">Friendly and Professional Health Care<br>For You and your Family</p>
    </section>

    <section class="panel panel--film">
      <div class="photo photo--desk" role="img" aria-label="Hands holding a clipboard beside a laptop"></div>
      <div class="headline" style="top:116px">
        <div class="red" style="font-size:15px">Book</div>
        <div class="blue" style="font-size:20px">ONLINE<span style="font-size:12px">at</span></div>
        <div class="red" style="font-family:Tinos,serif;font-size:4.3px;font-weight:400;margin-top:1px">www.wattlebrookmedicalpractice.example.au</div>
      </div>
      <div class="brand" style="top:192px">Wattlebrook Medical Practice</div>
      <div class="pulse" role="img" aria-label="Heartbeat line ornament"></div>
      <p class="motto" style="top:229px">Friendly and Professional Health Care<br>For You and your Family</p>
    </section>

    <section class="panel panel--film">
      <div class="photo photo--warm" role="img" aria-label="Coins and banknotes on a table"></div>
      <div class="headline" style="top:108px">
        <div class="red" style="font-size:15px">Bulk</div>
        <div class="blue" style="font-size:23px">BILLING</div>
        <div class="red" style="font-size:11px">for GP Services</div>
      </div>
      <div class="brand" style="top:192px">Wattlebrook Medical Practice</div>
      <div class="pulse" role="img" aria-label="Heartbeat line ornament"></div>
      <p class="motto" style="top:229px">Friendly and Professional Health Care<br>For You and your Family</p>
    </section>

    <section class="panel panel--tint">
      <div class="brand brand--tint" style="top:14px">Wattlebrook Medical Practice</div>
      <div class="tint-head" style="top:42px">Health Services Include:</div>
      <ul class="allied">
        <li>Psychology</li><li>Physiotherapy</li><li>Podiatry</li>
        <li>Dietetics and Nutrition</li><li>Exercise Physiology</li><li>Diabetes Education</li>
      </ul>
      <div class="pattern pattern--wide" role="img" aria-label="Faint molecular hexagon pattern with a red heartbeat line"></div>
    </section>

    <section class="panel panel--tint">
      <div class="brand brand--tint" style="top:14px">Wattlebrook Medical Practice</div>
      <div class="tint-head" style="top:42px;left:14px">Usual opening hours</div>
      <table class="hours">
        <tr><td>Monday</td><td>8.00am - 5.30pm</td></tr>
        <tr><td>Tuesday</td><td>8.00am - 9.00pm</td></tr>
        <tr><td>Wednesday</td><td>8.00am - 9.00pm</td></tr>
        <tr><td>Thursday</td><td>8.00am - 9.00pm</td></tr>
        <tr><td>Friday</td><td>8.00am - 9.00pm</td></tr>
        <tr><td>Saturday</td><td>8.00am - 4.00pm</td></tr>
        <tr><td>Sunday</td><td>8.00am -</td></tr>
        <tr><td>12.00noon</td><td></td></tr>
      </table>
      <p class="note">Public holidays: <span class="red">Closed</span></p>
      <svg style="position:absolute;left:52px;top:178px" width="60" height="10" viewBox="0 0 60 10">
        <rect x="1" y="3" width="54" height="4" rx="2" fill="#85abd2"/>
        <rect x="20" y="3" width="35" height="4" fill="#ec1f27"/>
        <circle cx="55" cy="5" r="3.5" fill="#ec1f27"/>
      </svg>
      <div class="pattern pattern--wide" role="img" aria-label="Faint molecular hexagon pattern"></div>
    </section>

    <section class="panel panel--tint">
      <div class="brand brand--tint" style="top:14px">Wattlebrook Medical Practice</div>
      <div class="tint-head" style="top:48px">Our Services Include:</div>
      <div class="pattern pattern--wide" role="img" aria-label="Faint molecular hexagon pattern with a red heartbeat line"></div>
      <ol class="services">
        <li><span>1.</span>General Practice<br>Consultations</li>
        <li><span>2.</span>Immunisations</li>
        <li><span>3.</span>Health checks</li>
        <li><span>4.</span>Women's health</li>
        <li><span>5.</span>Men's Health</li>
        <li><span>6.</span>Skin cancer checks</li>
        <li><span>7.</span>Travel medicine</li>
        <li><span>8.</span>Referrals</li>
        <li><span>9.</span>Antenatal checks</li>
        <li><span>10.</span>Minor surgery</li>
        <li><span>11.</span>Cosmetic medicine</li>
        <li><span>12.</span>Pre-Employment Medicals</li>
        <li><span>13.</span>Diabetes care</li>
        <li><span>14.</span>Wound care, and much more</li>
      </ol>
    </section>

    <section class="panel panel--tint">
      <div class="center-copy" style="top:40px">FLU SHOT<br>AVAILABLE NOW</div>
      <div class="center-copy" style="top:82px">BOOK AN APPOINTMENT</div>
      <div class="pattern pattern--wide" role="img" aria-label="Faint molecular hexagon pattern"></div>
    </section>

    <section class="panel panel--film">
      <div style="position:absolute;left:16px;top:18px;font-weight:900;line-height:.95;white-space:nowrap">
        <div class="blue" style="font-size:17px">Friendly<span class="red" style="font-size:10px">and</span></div>
        <div class="blue" style="font-size:14px">Professional</div>
        <div class="red" style="font-size:15px">Health Care</div>
        <div class="red" style="font-size:7px;font-weight:700;margin-top:2px">For You and your Family</div>
      </div>
      <div class="brand" style="top:86px">Wattlebrook Medical Practice</div>
      <svg class="cross" viewBox="0 0 20 20"><circle cx="10" cy="10" r="9.5" fill="#ec1f27"/><rect x="8" y="4" width="4" height="12" fill="#fff"/><rect x="4" y="8" width="12" height="4" fill="#fff"/></svg>
      <div class="photo photo--hands" role="img" aria-label="Family hands stacked together"></div>
    </section>

    <section class="panel panel--film">
      <div class="photo photo--clinic" role="img" aria-label="Blood pressure check with a cuff and gauge"></div>
      <div class="headline" style="top:136px">
        <div class="red" style="font-size:15px">Health</div>
        <div class="blue" style="font-size:23px">CHECKS</div>
      </div>
      <div class="brand" style="top:195px">Wattlebrook Medical Practice</div>
      <div class="pulse" role="img" aria-label="Heartbeat line ornament"></div>
      <p class="motto" style="top:229px">Friendly and Professional Health Care<br>For You and your Family</p>
    </section>

    <section class="panel panel--film">
      <div class="photo photo--desk" role="img" aria-label="Sugar bowl and blood glucose meter"></div>
      <div class="headline" style="top:110px">
        <div class="red" style="font-size:16px">Diabetes</div>
        <div class="blue" style="font-size:16px">EDUCATION</div>
        <div style="font-size:16px"><span class="red" style="font-size:11px">and</span><span class="blue">CARE</span></div>
      </div>
      <div class="brand" style="top:195px">Wattlebrook Medical Practice</div>
      <div class="pulse" role="img" aria-label="Heartbeat line ornament"></div>
      <p class="motto" style="top:229px">Friendly and Professional Health Care<br>For You and your Family</p>
    </section>

    <section class="panel panel--film">
      <div class="photo photo--clinic" role="img" aria-label="Doctor at a consultation desk"></div>
      <div class="headline" style="top:130px">
        <div class="red" style="font-size:15px">General</div>
        <div class="blue" style="font-size:13px">PRACTICE</div>
        <div class="blue" style="font-size:10.5px">CONSULTATIONS</div>
      </div>
      <div class="brand" style="top:195px">Wattlebrook Medical Practice</div>
      <div class="pulse" role="img" aria-label="Heartbeat line ornament"></div>
      <p class="motto" style="top:229px">Friendly and Professional Health Care<br>For You and your Family</p>
    </section>

  </div>
</div>
</body>
</html>
```